Cedar Ridge Strong Partners and Households Initiative-Teen

We need a flyer that invites high school students to our program. The students go through healthy relationship education, financial stability and workforce readiness.

We are in five locations, so we need a flyer that we can edit the text to update addresses, dates and any additional information based on our needs.

Attached are the two logo's we would like to use. I have also attached a previous flyer that we created to give you an idea of the text that is included.

In the past we have only promoted the healthy relationship component, but if you are able to incorporate finances (money) and job development (jobs), that would be great.

Industry/Entity Type

School

Requirements
Must have
• Targets high school students
• Make the text available for us to edit
• Our topics is healthy relationship, money and jobs

```html
<!DOCTYPE html>
<html lang="en">
<head>
<meta charset="utf-8">
<title>Cedar Ridge Strong Partners and Households Initiative-Teen – Workshops</title>
<link rel="stylesheet" href="https://fonts.googleapis.com/css2?family=Montserrat:wght@500;600;700&family=Roboto:wght@300;400&display=swap">
<style>
:root{
  --orange:#ff6a0d;
  --gold:#fbb635;
  --red:#c9202c;
  --maroon:#4a1531;
  --plum:#84204f;
  --teal:#1f8f9c;
  --lime:#a3b93a;
  --navy:#06304a;
  --ink:#1d2a2c;
  --white:#ffffff;
  --logo-navy:#1c3f7d;
  --logo-orange:#f0901e;
}
*{box-sizing:border-box;margin:0;padding:0}
html,body{width:927px;height:1200px;overflow:hidden;background:var(--white)}
.flyer{position:relative;width:927px;height:1200px;overflow:hidden;font-family:'Roboto',sans-serif;background:var(--navy)}
.hero-photo{position:absolute;left:0;top:0;width:927px;height:292px;
  background:linear-gradient(120deg,#b9a9a0 0%,#d8cdc6 35%,#8f8580 55%,#5a6e66 70%,#c7bdb6 100%)}
.logo-box{position:absolute;top:14px;height:150px;background:rgba(255,255,255,.9);
  display:flex;align-items:center;justify-content:center;gap:12px;text-align:center}
.logo-box.partner{left:40px;width:354px}
.logo-box.agency{left:508px;width:355px}
.logo-mark{width:26px;height:26px;border-radius:50%;flex:none}
.partner .logo-mark{background:var(--logo-orange)}
.agency .logo-mark{background:var(--red)}
.logo-name{font-family:'Montserrat',sans-serif;font-weight:600;font-size:19px;line-height:1.25}
.partner .logo-name{color:var(--logo-orange);width:250px}
.agency .logo-name{color:var(--logo-navy);width:250px}
.headline{position:absolute;left:407px;top:212px;width:520px;height:80px;background:var(--orange);
  color:var(--white);font-family:'Montserrat',sans-serif;font-weight:700;text-align:center;padding-top:12px}
.headline .line1{font-size:24px;line-height:1.2}
.headline .line2{font-size:17.5px;margin-top:6px;letter-spacing:.3px}
.topic-band{position:absolute;left:0;top:292px;width:927px;height:48px;background:var(--gold)}
.topic-tab{position:absolute;top:292px;height:39px;color:var(--white);font-family:'Montserrat',sans-serif;
  font-weight:600;font-size:16px;letter-spacing:.6px;display:flex;align-items:center;justify-content:center}
.topic-tab.relationship{left:84px;width:242px;background:var(--red)}
.topic-tab.money{left:407px;width:227px;background:var(--maroon)}
.topic-tab.jobs{left:716px;width:211px;background:var(--teal)}
.topic-col{position:absolute;top:340px;height:260px;padding:26px 24px 0;color:#f3e6e8;
  font-weight:300;font-size:14.4px;line-height:21px;text-align:justify}
.topic-col.relationship{left:0;width:327px;background:var(--red)}
.topic-col.money{left:327px;width:308px;background:radial-gradient(circle at 50% 50%,#9b2a5d,var(--maroon) 90%)}
.topic-col.jobs{left:635px;width:292px;background:radial-gradient(circle at 50% 45%,#29a4b1,#187f8b 90%)}
.includes{position:absolute;left:0;top:600px;width:327px;height:500px;background:var(--lime);padding:32px 24px 0}
.includes h2{font-family:'Montserrat',sans-serif;font-weight:600;font-size:22px;color:#111;letter-spacing:.3px}
.includes .intro{color:#eef3d6;font-weight:300;font-size:14.4px;line-height:21px;margin-top:6px;text-align:justify}
.includes ul{list-style:none;margin:20px 0 0 16px;color:var(--white);font-weight:300;font-size:18.5px;line-height:24px}
.includes li{margin-bottom:25px}
.schedule{position:absolute;left:395px;top:628px;width:500px;color:var(--white)}
.schedule h2{font-family:'Montserrat',sans-serif;font-weight:600;font-size:21.5px;line-height:24px}
.schedule .when{font-family:'Montserrat',sans-serif;font-weight:500;font-size:19.5px;line-height:24px;color:var(--ink);margin-top:26px}
.locations{position:absolute;left:395px;top:764px;width:500px;display:grid;grid-template-columns:255px 245px;row-gap:18px}
.location h3{font-family:'Montserrat',sans-serif;font-weight:600;font-size:17px;color:var(--white);margin-bottom:22px}
.location p{font-family:'Roboto',sans-serif;font-size:14.4px;line-height:24.5px;color:var(--ink)}
.footer-curve{position:absolute;left:0;top:1080px;width:927px;height:120px}
.funding{position:absolute;left:48px;top:1139px;width:831px;height:53px;border:1.5px solid var(--lime);
  background:var(--white);color:#222;font-size:12.6px;line-height:16.5px;text-align:center;padding:6px 8px}
</style>
</head>
<body>
<main class="flyer">
  <div class="hero-photo" role="img" aria-label="Photo of a student carrying a tall stack of books"></div>

  <div class="logo-box partner">
    <span class="logo-mark"></span>
    <span class="logo-name">Cedar Ridge Strong Partners</span>
  </div>
  <div class="logo-box agency">
    <span class="logo-mark"></span>
    <span class="logo-name">Harborview Community Outreach Alliance</span>
  </div>

  <div class="headline">
    <div class="line1">Workshops for High School students on</div>
    <div class="line2">HEALTHY RELATIONSHIP, MONEY &amp; JOBS</div>
  </div>

  <div class="topic-band"></div>
  <div class="topic-tab relationship">HEALTHY RELATIONSHIP</div>
  <div class="topic-tab money">MONEY</div>
  <div class="topic-tab jobs">JOBS</div>

  <section class="topic-col relationship">Lorem Ipsum is simply dummy text of the printing and typesetting industry. Lorem Ipsum has been the industry's standard dummy text ever since the 1500s, when an unknown printer took a galley of type and scrambled it to make a type specimen book. It has survived not only five centuries, but also the leap into electronic typesetting.</section>
  <section class="topic-col money">Lorem Ipsum is simply dummy text of the printing and typesetting industry. Lorem Ipsum has been the industry's standard dummy text ever since the 1500s, when an unknown printer took a galley of type and scrambled it to make a type specimen book. It has survived not only five centuries, but also the leap into electronic typesetting.</section>
  <section class="topic-col jobs">Lorem Ipsum is simply dummy text of the printing and typesetting industry. Lorem Ipsum has been the industry's standard dummy text ever since the 1500s, when an unknown printer took a galley of type and scrambled it to make a type specimen book. It has survived not only five centuries, but also the leap into electronic typesetting.</section>

  <section class="includes">
    <h2>TOP INCLUDES</h2>
    <p class="intro">Lorem Ipsum is simply dummy text of the printing and typesetting industry. Lorem Ipsum has been the industry's standard dumm text.</p>
    <ul>
      <li>Recognizing signs and types of abuse</li>
      <li>Building healthy&nbsp; relationships Self-esteem</li>
      <li>Safety Planning</li>
      <li>How to get help and where</li>
    </ul>
  </section>

  <section class="schedule">
    <h2>Workshops will be held every Wednesday<br>for 10 weeks starting</h2>
    <p class="when">January 10th.<br>From 5:30pm–7:30pm</p>
  </section>

  <section class="locations">
    <div class="location"><h3>Address 1</h3><p>Marisol Vega, CR-SPH<br>Program Coordinator<br>Phone: 555-204-3187<br>E-mail: mvega@hcoa.org</p></div>
    <div class="location"><h3>Address 2</h3><p>Marisol Vega, CR-SPH<br>Program Coordinator<br>Phone: 555-204-3187<br>E-mail: mvega@hcoa.org</p></div>
    <div class="location"><h3>Address 3</h3><p>Marisol Vega, CR-SPH<br>Program Coordinator<br>Phone: 555-204-3187<br>E-mail: mvega@hcoa.org</p></div>
    <div class="location"><h3>Address 4</h3><p>Marisol Vega, CR-SPH<br>Program Coordinator<br>Phone: 555-204-3187<br>E-mail: mvega@hcoa.org</p></div>
  </section>

  <svg class="footer-curve" viewBox="0 0 927 120" preserveAspectRatio="none" aria-hidden="true">
    <path d="M0 48 Q420 -10 927 60 L927 120 L0 120 Z" fill="#04283e"/>
    <path d="M0 48 Q420 -10 927 60" fill="none" stroke="#a3b93a" stroke-width="1.5"/>
  </svg>

  <p class="funding">“Funding for this project was provided by the Regional Department of Family Services, Office for Youth and Households, Grant: #47KT2291.&nbsp; These services are available to all eligible persons, regardless of race, gender, age, disability, or religion.”</p>
</main>
</body>
</html>
```